Electronic Refurbishment Warehouse needs a Website

We are looking for a clean, professional looking design with iconic imagery. Our main point we want to get across is that we will help clients save time, and money, and provide outstanding quality. Our logo can be found in the uploads section. This site is used to impress clients that we have a pre-existing relationship with. This site will be available for the public but it will not be used to advertise to the public or to drive traffic to it. The color scheme we are looking to stay with is blue, but that is not to say that everything should be a shade of blue. Last note, see site map below.

Site Map:

Home
Company
a. company overview
b. CEO letter
Services
a. Remanufacture & Refurbishment Services
1. Consumer Electronics
2. Cellular Phones
b.Reverse Logistics Management
c.Warranty Repair & Field Services
d.Quality Control & Assurance
e.Warehousing & Distribution
Careers
Contact Us
Updates

Project Deadline Extended
Reason: We want to allocate more time for designers to do what they do best.

Target Market(s)

Phone and TV Retailers that may have units that need to be refurbished. Example Vorelli, tradequay, qlm, etc.

Industry/Entity Type

Electronics

Requirements
Must have
• Home Page Slider.
Iconic imagery and navigation.
The ability to be put into the 960 Grid.

```html
<!DOCTYPE html>
<html lang="en">
<head>
<meta charset="utf-8">
<title>Norvane Group – Repair and Refurbishment</title>
<link href="https://fonts.googleapis.com/css2?family=PT+Sans:wght@400;700&family=Arimo:wght@400;700&display=swap" rel="stylesheet">
<style>
:root{
  --ink:#0a1a2a;
  --nav-dark:#1b1b1b;
  --nav-mid:#2e2e2e;
  --btn-blue:#1a8fd0;
  --hero-top:#0a6fbf;
  --hero-mid:#1788da;
  --hero-low:#0f73c6;
  --band:#3aa6e6;
  --band-low:#52b6ef;
  --grey-strip:#c4c4c4;
  --cream:#f3f1e6;
  --foot-dark:#0b2338;
  --foot-line:#0f7fd4;
  --white:#ffffff;
  --text-dark:#0d2c45;
}
*{margin:0;padding:0;box-sizing:border-box}
html,body{width:1200px;height:1001px;overflow:hidden}
body{position:relative;background:var(--cream);font-family:"Arimo",Arial,sans-serif;color:var(--ink)}
.abs{position:absolute}
.top-strip{left:0;top:0;width:1200px;height:46px;background:linear-gradient(#0b3f6a,#0c5a93)}
.hero{left:0;top:45px;width:1200px;height:348px;background:radial-gradient(ellipse at 40% 20%,#2ea0ea 0%,var(--hero-mid) 35%,var(--hero-low) 80%,#0b62ad 100%)}
.nav{left:165px;top:0;width:865px;height:61px;border-radius:0 0 6px 6px;background:linear-gradient(var(--nav-mid),var(--nav-dark));box-shadow:0 3px 6px rgba(0,0,0,.4);display:flex;align-items:center;padding-left:16px}
.nav a{color:var(--white);text-decoration:none;font-size:17px;margin-right:33px;line-height:31px}
.nav a.current{background:linear-gradient(#2aa8e6,#1378bf);border-radius:5px;padding:0 13px;margin-right:33px;box-shadow:inset 0 1px 0 rgba(255,255,255,.3)}
.search{position:absolute;right:20px;top:18px;display:flex;align-items:center}
.search label{color:var(--white);font-size:17px;margin-right:10px}
.search .field{width:183px;height:25px;background:#555;border:1px solid #666;border-radius:2px;color:#aaa;font-size:10px;line-height:23px;padding-left:36px;position:relative}
.search .field svg{position:absolute;left:12px;top:6px}
.search .go{margin-left:6px;width:41px;height:26px;background:var(--btn-blue);color:var(--white);font-size:14px;text-align:center;line-height:26px;border-radius:2px}
.hero-title{left:230px;top:132px;color:var(--white);font-family:"PT Sans",sans-serif;font-weight:700;line-height:25px;text-shadow:0 1px 2px rgba(0,0,0,.3)}
.hero-title .l1{font-size:28px;display:block}
.hero-title .l2{font-size:24px;display:block}
.hero-copy{left:230px;top:208px;width:410px;color:var(--white);font-size:13.4px;line-height:17px}
.hero-copy p{margin-bottom:24px}
.phones{left:652px;top:93px;width:323px;height:282px;border-radius:12px;background:linear-gradient(135deg,#2a2a2a,#5a5a5a 40%,#1d1d1d)}
.arrow{top:195px}
.arrow.left{left:168px}
.arrow.right{left:995px}
.band{left:0;top:393px;width:1200px;height:198px;background:linear-gradient(var(--band),var(--band-low))}
.chevron{left:298px;top:357px}
.band-phone{left:193px;top:415px;width:157px;height:152px;border-radius:14px;background:linear-gradient(#1f3a6e,#223f7b 60%,#2d58a3)}
.welcome-title{left:373px;top:427px;color:var(--white);font-family:"PT Sans",sans-serif;font-weight:700;font-size:25px}
.welcome-rule{left:373px;top:465px;width:643px;height:1px;background:rgba(10,60,110,.35)}
.welcome-copy{left:376px;top:477px;width:640px;color:var(--text-dark);font-size:11.4px;line-height:15px}
.more{left:375px;top:550px;color:var(--ink);font-size:11.5px;display:flex;align-items:center;gap:7px}
.grey-strip{left:0;top:591px;width:1200px;height:12px;background:var(--grey-strip)}
.card{top:637px;width:261px;height:150px;border:1px solid #8ba3bf;border-radius:2px;overflow:hidden}
.card .label{position:absolute;color:var(--white);font-family:"Arimo",Arial,sans-serif;font-weight:700;text-shadow:0 1px 3px rgba(0,0,0,.6);letter-spacing:-.5px}
.card-reman{left:166px;background:linear-gradient(120deg,#0d3f86,#2f7ad1 55%,#8cc0ef)}
.card-career{left:467px;background:linear-gradient(#6b6862,#8a8478 60%,#3c3a36)}
.card-logistics{left:768px;background:linear-gradient(#5a6e82,#2f4a63 45%,#23425c)}
.card .shade{position:absolute;left:0;right:0;bottom:0}
.footer-line{left:0;top:823px;width:1200px;height:8px;background:var(--foot-line)}
.footer{left:0;top:831px;width:1200px;height:88px;background:var(--foot-dark)}
.svc{top:857px;display:flex;align-items:center;gap:12px;color:var(--white);font-size:13.6px;line-height:17px}
.bottom-links{left:166px;top:937px;font-size:11.6px;color:var(--ink)}
.copyright{left:166px;top:955px;font-size:11.6px;color:var(--ink)}
.logo-box{left:845px;top:920px;width:146px;height:68px;background:var(--white);box-shadow:0 1px 5px rgba(0,0,0,.35);display:flex;align-items:center;justify-content:center;gap:6px}
.logo-box .mark{width:14px;height:14px;background:#2d7fc4}
.logo-box span{font-family:"PT Sans",sans-serif;font-size:17px;color:#3f5e80;font-weight:700}
</style>
</head>
<body>
<div class="abs top-strip"></div>
<div class="abs hero"></div>

<nav class="abs nav">
  <a href="#" class="current">Home</a>
  <a href="#">Company</a>
  <a href="#">Services</a>
  <a href="#">Careers</a>
  <a href="#">Contact Us</a>
  <div class="search">
    <label>Search</label>
    <div class="field"><svg width="11" height="11" viewBox="0 0 11 11"><circle cx="6.5" cy="4.5" r="3" fill="none" stroke="#ccc" stroke-width="1.4"/><line x1="4.3" y1="6.7" x2="1" y2="10" stroke="#ccc" stroke-width="1.6"/></svg>enter your text here...</div>
    <div class="go">Go</div>
  </div>
</nav>

<h1 class="abs hero-title"><span class="l1">Repair and Refurbishment Services</span><span class="l2">for Electronics Components</span></h1>
<div class="abs hero-copy">
  <p>Lorem ipsum dolor sit amet, consectetur adipiscing elit. Vivamus orci mauris, ultricies sed pellentesque eleifend, mollis vitae mauris. Nullam eu mi quis quam faucibus rutrum eu id lectus.</p>
  <p>Aliquam erat volutpat. Aenean in mattis enim. Donec sed nulla sed leo consequat fermentum nec id mauris.</p>
</div>
<div class="abs phones" role="img" aria-label="Three smartphones showing a messaging app"></div>

<svg class="abs arrow left" width="40" height="44" viewBox="0 0 40 44"><path d="M34 2 L8 22 L34 42 L26 22 Z" fill="#6fb0e0" opacity=".8"/></svg>
<svg class="abs arrow right" width="40" height="44" viewBox="0 0 40 44"><path d="M6 2 L32 22 L6 42 L14 22 Z" fill="#6fb0e0" opacity=".8"/></svg>

<div class="abs band"></div>
<svg class="abs chevron" width="220" height="52" viewBox="0 0 220 52"><path d="M0 0 L110 36 L220 0 L190 0 L110 26 L30 0 Z" fill="#fff"/><path d="M30 0 L110 26 L190 0 Z" fill="#fff"/><path d="M100 36 L110 52 L120 36 Z" fill="#2a8fdc"/></svg>

<div class="abs band-phone" role="img" aria-label="Slider phone with keyboard and photo on screen"></div>
<h2 class="abs welcome-title">Welcome to Norvane Group</h2>
<div class="abs welcome-rule"></div>
<p class="abs welcome-copy">Lorem ipsum dolor sit amet, consectetur adipiscing elit. Vivamus orci mauris, ultricies sed pellentesque eleifend, mollis vitae mauris. Nullam eu mi quis quam faucibus rutrum eu id lectus. Aliquam erat volutpat. Aenean in mattis enim. Donec sed nulla sed leo consequat fermentum nec id mauris.</p>
<div class="abs more"><svg width="5" height="8" viewBox="0 0 5 8"><path d="M0 0 L5 4 L0 8Z" fill="#0a1a2a"/></svg>Click here for more information...</div>

<div class="abs grey-strip"></div>

<div class="abs card card-reman" role="img" aria-label="Mobile phone with headset on blue background">
  <div class="shade" style="height:38px;background:rgba(40,110,200,.35)"></div>
  <div class="label" style="left:115px;top:48px;font-size:17px;line-height:18px">Remanufacture &amp;<br>Refurbishment<br><span style="font-size:22px;line-height:22px">Services</span></div>
  <div class="label" style="left:140px;top:127px;font-size:17px">Click here</div>
</div>
<div class="abs card card-career" role="img" aria-label="Employee in white coat in a warehouse">
  <div class="shade" style="height:56px;background:rgba(30,30,30,.7)"></div>
  <div class="label" style="left:9px;top:106px;font-size:22px">Career Opportunities</div>
  <div class="label" style="left:11px;top:132px;font-size:13px">Our employees are the key to our success</div>
</div>
<div class="abs card card-logistics" role="img" aria-label="Cargo ship at sea">
  <div class="shade" style="height:30px;background:rgba(255,255,255,.2)"></div>
  <div class="label" style="left:17px;top:63px;font-size:22px;line-height:22px">Reverse Logistics<br><span style="font-size:27px;line-height:24px">Management</span></div>
  <div class="label" style="left:18px;top:126px;font-size:17px">Click here</div>
</div>

<div class="abs footer-line"></div>
<div class="abs footer"></div>

<div class="abs svc" style="left:175px">
  <svg width="34" height="34" viewBox="0 0 34 34"><path d="M4 30 L26 8" stroke="#d8dde2" stroke-width="4"/><path d="M8 6 L30 28" stroke="#aab4bd" stroke-width="3"/><circle cx="28" cy="6" r="4" fill="none" stroke="#d8dde2" stroke-width="3"/></svg>
  <div>Remanufacture &amp;<br>Refurbishment Services</div>
</div>
<div class="abs svc" style="left:389px">
  <svg width="46" height="40" viewBox="0 0 46 40"><rect x="14" y="4" width="30" height="22" fill="#e8ecef"/><path d="M2 14 H14 V30 H2 Z" fill="#f39a1c"/><rect x="2" y="26" width="42" height="4" fill="#c9cdd0"/><circle cx="9" cy="33" r="4" fill="#333"/><circle cx="36" cy="33" r="4" fill="#333"/></svg>
  <div>Reverse Logistics<br>Management</div>
</div>
<div class="abs svc" style="left:567px">
  <svg width="44" height="44" viewBox="0 0 44 44"><circle cx="22" cy="22" r="21" fill="#c4232b"/><circle cx="22" cy="22" r="13" fill="#e3a520"/></svg>
  <div>Warranty Repair<br>&amp; Field Services</div>
</div>
<div class="abs svc" style="left:746px">
  <svg width="32" height="32" viewBox="0 0 32 32"><rect x="3" y="3" width="24" height="26" fill="#e6edf4" stroke="#7aa7cf"/><line x1="7" y1="10" x2="22" y2="10" stroke="#4a86c0" stroke-width="2"/><line x1="7" y1="16" x2="22" y2="16" stroke="#4a86c0" stroke-width="2"/><circle cx="24" cy="24" r="5" fill="#f0b21e"/></svg>
  <div>Quality Control<br>&amp; Assurance</div>
</div>
<div class="abs svc" style="left:897px">
  <svg width="32" height="32" viewBox="0 0 32 32"><rect x="2" y="2" width="28" height="28" fill="#dfe3e6" stroke="#fff"/><rect x="7" y="12" width="12" height="13" fill="none" stroke="#555" stroke-width="2"/><rect x="13" y="7" width="12" height="12" fill="none" stroke="#555" stroke-width="2"/></svg>
  <div>Warehousing<br>&amp; Distribution</div>
</div>

<div class="abs bottom-links">Home &nbsp;--&nbsp; Company &nbsp;--&nbsp; Services &nbsp;--&nbsp; Careers &nbsp;--&nbsp; Contact Us</div>
<div class="abs copyright">Norvane Group, Inc. © 2012, &nbsp;All rights reserved.</div>
<div class="abs logo-box"><div class="mark"></div><span>norvane group</span></div>
</body>
</html>
```